THE GRAND DELTA GROOVE REVUE---a CONCERT

We need a web page to support our upcoming concert asap. It is a southern blues concert featuring Odessa Brantley, Whitfield, Marvell Gaddis, and Reuben Oakes. We have as special guest local talent from the Augusta, Ga Area---Calloway, Abe Lark and Jo'Vanna. Hosted By: Augusta's Own--Brave Pecan.
The concert is as follow:
The Grand Bayou Lantern Revue
Saturday, July 7, 2018
7:00 pm Doors open at 6:00pm
Harlow Civic Hall, Augusta, GA
Tickets are $39, $49 and $59
Tickets on sale at the Box Office(need link to "BUY TICKETS"), Zenith Records, Marigold Box Office and Camp Hollister, GA
We are honoring all military and first responders and offering discount tickets--contact 770-555-0182 for discount code
Overnight concert guests are invited to stay at the Restwell Lodge in Augusta for a reduced rate of $69--we would like a link to that site. Mention Code:
The Concert is promoted by QUARTZ MERIDIAN ENTERTAINMENT
The Harlow Civic Hall Logo and Adress must appear somewhere at the bottom or near where the Harlow Civic Hall is mentioned.
The Military requires that we say, No government or military endorsement implied.
Picture of the Artists and our current flyer is attached. If you need the layered file--contact us

Target Market(s)

blues music lovers and concert goers

Requirements
Must have
• link to buy tickets/mention chatterly and peepline
Nice to have
• links to artist sites and hotel, TICKET GIVEAWAY REGISTRATION

```html
<!DOCTYPE html>
<html lang="en">
<head>
<meta charset="utf-8">
<title>The Grand Bayou Lantern Revue</title>
<link rel="stylesheet" href="https://fonts.googleapis.com/css2?family=Arvo&family=Cinzel:wght@700&family=Playfair+Display:wght@700&display=swap">
<style>
  :root {
    --nav-bg: #0a0820;
    --nav-text: #e9c97a;
    --title-gold: #ecd08f;
    --orange: #fd8f3a;
    --orange-deep: #f47a1a;
    --divider: #ffc48e;
    --dark-strip: #4a1414;
    --pink: #f1218b;
    --white: #ffffff;
  }
  * { margin: 0; padding: 0; box-sizing: border-box; }
  html, body { width: 1200px; height: 704px; overflow: hidden; background: var(--nav-bg); }
  .page { position: relative; width: 1200px; height: 704px; overflow: hidden; }

  .site-nav {
    position: absolute; top: 0; left: 0; width: 1200px; height: 53px;
    background: var(--nav-bg); display: flex; justify-content: center; align-items: center;
    z-index: 2;
  }
  .site-nav a {
    font-family: "Arvo", serif; font-size: 13.5px; color: var(--nav-text);
    text-decoration: none; margin: 0 25px;
  }

  .hero { position: absolute; top: 53px; left: 0; width: 1200px; height: 554px; }
  .hero-photo {
    position: absolute; inset: 0;
    background:
      radial-gradient(ellipse 260px 200px at 160px 260px, rgba(215,210,235,.95), transparent 70%),
      radial-gradient(ellipse 240px 180px at 470px 180px, rgba(210,205,235,.7), transparent 70%),
      radial-gradient(ellipse 200px 200px at 780px 220px, rgba(200,195,230,.6), transparent 70%),
      radial-gradient(ellipse 260px 140px at 620px 420px, rgba(170,170,235,.7), transparent 70%),
      linear-gradient(180deg, #3a0c22 0%, #8e1c3c 35%, #6a2450 62%, #2a1424 85%, #140a14 100%);
  }
  .hero-crowd {
    position: absolute; left: 0; right: 0; bottom: 0; height: 130px;
    background: linear-gradient(180deg, transparent 0%, rgba(30,20,30,.85) 45%, #1a1018 100%);
  }

  .hero-title {
    position: absolute; left: 0; top: 0; width: 1200px; height: 554px;
    font-family: "Cinzel", serif; font-weight: 700; color: var(--title-gold); line-height: 1;
  }
  .hero-title span { position: absolute; left: 0; width: 1200px; text-align: center; white-space: nowrap; }
  .hero-title .line-small { top: 200px; font-size: 30px; }
  .hero-title .line-wide { top: 226px; font-size: 52px; }
  .hero-title .line-huge { top: 268px; font-size: 120px; letter-spacing: 2px; }

  .slide-arrow { position: absolute; top: 199px; width: 84px; height: 84px; }
  .slide-arrow.prev { left: 19px; }
  .slide-arrow.next { right: 45px; }

  .countdown-bar { position: absolute; left: 0; top: 608px; width: 1200px; height: 96px; display: flex; }
  .countdown { width: 576px; height: 96px; background: var(--orange); position: relative; }
  .count-unit { position: absolute; top: 0; width: 90px; height: 96px; margin-left: -45px; text-align: center; color: var(--white); }
  .count-unit .num {
    position: absolute; left: 0; right: 0; top: 6px;
    font-family: "Playfair Display", serif; font-weight: 700; font-size: 50px; line-height: 1.05;
    font-variant-numeric: lining-nums;
  }
  .count-unit .label {
    position: absolute; left: 0; right: 0; top: 64px;
    font-family: "Playfair Display", serif; font-weight: 700; font-size: 12.5px; letter-spacing: 1.5px;
  }
  .count-divider { position: absolute; top: 22px; width: 1px; height: 48px; background: var(--divider); }

  .scroll-toggle { width: 39px; height: 96px; background: var(--dark-strip); display: flex; align-items: center; justify-content: center; }
  .join-cta {
    flex: 1; background: var(--pink); display: flex; align-items: center; padding-left: 41px;
    font-family: "Playfair Display", serif; font-weight: 700; font-size: 37px; color: var(--white);
    text-decoration: none; letter-spacing: .5px;
  }
</style>
</head>
<body>
<div class="page">
  <nav class="site-nav">
    <a href="#">Home</a>
    <a href="#">Event</a>
    <a href="#">Peformers</a>
    <a href="#">Special Guest</a>
    <a href="#">Tickets</a>
    <a href="#">Offers</a>
    <a href="#">Directions</a>
    <a href="#">Contact</a>
  </nav>

  <section class="hero">
    <div class="hero-photo" role="img" aria-label="Concert stage with spotlights, red and white haze and a cheering crowd with raised hands"></div>
    <div class="hero-crowd"></div>

    <h1 class="hero-title">
      <span class="line-small">The Grand</span>
      <span class="line-wide">BAYOU LANTERN</span>
      <span class="line-huge">REVUE</span>
    </h1>

    <svg class="slide-arrow prev" viewBox="0 0 84 84" aria-label="Previous slide">
      <rect x="14" y="14" width="56" height="56" transform="rotate(45 42 42)" fill="var(--orange)" opacity=".45"/>
      <rect x="21" y="21" width="42" height="42" transform="rotate(45 42 42)" fill="var(--orange-deep)"/>
      <polyline points="46,32 36,42 46,52" fill="none" stroke="var(--white)" stroke-width="5" stroke-linecap="round" stroke-linejoin="round"/>
    </svg>
    <svg class="slide-arrow next" viewBox="0 0 84 84" aria-label="Next slide">
      <rect x="14" y="14" width="56" height="56" transform="rotate(45 42 42)" fill="var(--orange)" opacity=".45"/>
      <rect x="21" y="21" width="42" height="42" transform="rotate(45 42 42)" fill="var(--orange-deep)"/>
      <polyline points="38,32 48,42 38,52" fill="none" stroke="var(--white)" stroke-width="5" stroke-linecap="round" stroke-linejoin="round"/>
    </svg>
  </section>

  <div class="countdown-bar">
    <div class="countdown">
      <div class="count-unit" style="left:176px"><span class="num">00</span><span class="label">DAYS</span></div>
      <div class="count-divider" style="left:230px"></div>
      <div class="count-unit" style="left:289px"><span class="num">00</span><span class="label">HRS</span></div>
      <div class="count-divider" style="left:347px"></div>
      <div class="count-unit" style="left:403px"><span class="num">00</span><span class="label">MIN</span></div>
      <div class="count-divider" style="left:463px"></div>
      <div class="count-unit" style="left:518px"><span class="num">00</span><span class="label">SEC</span></div>
    </div>
    <div class="scroll-toggle">
      <svg width="24" height="16" viewBox="0 0 24 16" aria-label="Scroll down">
        <polyline points="3,4 12,12 21,4" fill="none" stroke="var(--white)" stroke-width="4" stroke-linecap="round" stroke-linejoin="round"/>
      </svg>
    </div>
    <a class="join-cta" href="#">+ JOIN THE EVENTS</a>
  </div>
</div>
</body>
</html>
```